Harrowgate Estates Business Card for Apartment Buildings

Create business cards for resident managers who run apartment buildings. The audience is the public who are searching for apartment rentals, and current residents who live at the apartment building. Key design element will be incorporating the company logo, however, the logo cannot dominate. The building name and manager name are more important than the logo. Current business card design leaves little room for copy, so we may need to reduce the size on the current card to allow for more space for copy.

Target Market(s)

Adults 18-65 years of age, who are looking for an apartment rental, plus current residents who live at our apartment buildings.

Industry/Entity Type

Property Management

Contact Information for Business Card

A major design element will be use of the company logo. Important property and manager contact information must be part of the design. The size of the logo will need to be reduced to make room for building and manager contact copy.

Font styles to use
Sans Serif

Colors
3176b5
000000
959595
ffffff

Requirements
Must have
• 1) Incorporate the company logo.
• 2) Use the company colors (dark blue, black/grey, over white).
• 3) FEATURE THE BUILDING NAME
• 4) FEATURE THE MANAGER NAME
• 5) The company name is less important than BUILDING and MANAGER
• 6) Manager contact information
• **SEE ATTACHED CREATIVE BRIEF**
Nice to have
• 1) Back of card logo watermark
• 2) Ability to write notes on back of carfd
Should not have
• Avoid letting the company logo dominate the card, the building name and manager are more important than the company logo.

```html
<!DOCTYPE html>
<html lang="en">
<head>
<meta charset="utf-8">
<title>Harrowgate Estates – Resident Manager Business Card</title>
<link href="https://fonts.googleapis.com/css2?family=Lato:wght@400;700;900&display=swap" rel="stylesheet">
<style>
  :root {
    --brand-blue: #3176b5;
    --ink: #000000;
    --charcoal: #4a4a4c;
    --mid-grey: #959595;
    --paper: #ffffff;
    --backdrop: #e4e6e6;
    --watermark-grey: #e6e6e6;
    --watermark-blue: #dfe6f3;
  }
  * { box-sizing: border-box; margin: 0; padding: 0; }
  html, body {
    width: 1200px; height: 1000px; overflow: hidden;
    background: var(--backdrop);
    font-family: "Lato", Arial, sans-serif;
  }
  .canvas { position: relative; width: 1200px; height: 1000px; }
  .card {
    position: absolute; left: 320px; width: 560px; height: 320px;
    background: var(--paper);
    box-shadow: 0 6px 18px rgba(0,0,0,0.25);
    overflow: hidden;
  }
  .card--front { top: 140px; }
  .card--back { top: 540px; }
  .card svg.shapes { position: absolute; inset: 0; }

  .brand {
    position: absolute; left: 150px; top: 22px;
    color: var(--brand-blue); font-weight: 900; line-height: 1;
  }
  .brand__line1 { font-size: 36px; letter-spacing: 0.5px; }
  .brand__line2 { font-size: 14px; letter-spacing: 3.2px; margin-top: 2px; }

  .property { position: absolute; left: 168px; top: 118px; color: var(--ink); }
  .property__name { font-size: 21px; font-weight: 700; }
  .property__address { font-size: 16px; font-weight: 400; margin-top: 3px; color: #222; }
  .property__address span { color: var(--mid-grey); padding: 0 6px; }

  .manager__name {
    position: absolute; left: 22px; top: 190px;
    color: var(--paper); font-size: 25px; font-weight: 900; letter-spacing: 0.5px;
  }
  .manager__title {
    position: absolute; left: 28px; top: 231px;
    color: var(--paper); font-size: 16px; font-weight: 700;
  }
  .contact {
    position: absolute; left: 0; right: 0; top: 266px;
    text-align: center; color: #222; font-size: 15px; line-height: 1.45;
  }
  .contact span.sep { color: var(--mid-grey); padding: 0 6px; }

  .watermark-name {
    position: absolute; left: 120px; top: 130px;
    font-size: 40px; font-weight: 900; color: var(--watermark-blue);
    letter-spacing: 1px;
  }
</style>
</head>
<body>
<main class="canvas">

  <section class="card card--front" aria-label="Business card front">
    <svg class="shapes" width="560" height="320" viewBox="0 0 560 320" aria-hidden="true">
      <defs>
        <filter id="panel-shadow" x="-10%" y="-10%" width="120%" height="140%">
          <feDropShadow dx="0" dy="3" stdDeviation="3" flood-color="#000" flood-opacity="0.22"/>
        </filter>
      </defs>
      <!-- blue side block -->
      <rect x="0" y="62" width="80" height="190" fill="var(--brand-blue)"/>
      <!-- header panel -->
      <rect x="80" y="0" width="480" height="106" fill="var(--paper)" filter="url(#panel-shadow)"/>
      <rect x="0" y="0" width="80" height="62" fill="var(--paper)"/>
      <!-- rule under company name -->
      <line x1="150" y1="96" x2="468" y2="68" stroke="var(--brand-blue)" stroke-width="3"/>
      <!-- manager name band -->
      <polygon points="0,182 420,182 395,226 0,226" fill="var(--charcoal)" filter="url(#panel-shadow)"/>
      <!-- title band -->
      <polygon points="0,226 250,226 236,254 0,254" fill="var(--brand-blue)"/>
      <!-- plain brand circle -->
      <circle cx="96" cy="124" r="48" fill="var(--paper)" filter="url(#panel-shadow)"/>
    </svg>

    <div class="brand">
      <div class="brand__line1">HARROWGATE</div>
      <div class="brand__line2">ESTATES LLC</div>
    </div>

    <div class="property">
      <div class="property__name">Linden Court Apartments</div>
      <div class="property__address">2480 Maple Row<span>|</span>Riverton, CA 90210</div>
    </div>

    <div class="manager__name">MARISOL DELGADO</div>
    <div class="manager__title">Resident Manager</div>

    <div class="contact">
      <div>Office: 555-210-4471<span class="sep">|</span>Fax: 555-210-4472<span class="sep">|</span>Cell: 555-380-9156</div>
      <div>Email: marisol@harrowgateest.com</div>
    </div>
  </section>

  <section class="card card--back" aria-label="Business card back">
    <svg class="shapes" width="560" height="320" viewBox="0 0 560 320" aria-hidden="true">
      <circle cx="280" cy="150" r="170" fill="none" stroke="var(--watermark-grey)" stroke-width="22"/>
    </svg>
    <div class="watermark-name">HARROWGATE</div>
  </section>

</main>
</body>
</html>
```